Brightpath Desk letterhead and envelope

Design a formal (8.5x11) letterhead and envelope for sales outreach and legal matters. Using design input from https://www.brightpathdesk.com/ and the attached documents.

Industry/Entity Type

Software Service

Requirements
Must have
• These 4 hex colors are our official colors:
• #355c98 [blue]
• #1eb1a2 [teal]
• #fdba12 [gold]
• #f1653b [orange]
• So no other colors besides these should be used.

```html
<!DOCTYPE html>
<html lang="en">
<head>
<meta charset="utf-8">
<title>Brightpath Desk Letterhead</title>
<link href="https://fonts.googleapis.com/css2?family=Questrial&display=swap" rel="stylesheet">
<style>
  :root {
    --brand-blue: #355c98;
    --paper: #ffffff;
    --backdrop: #dfe6f2;
    --ink: #3a3f4a;
  }
  * { margin: 0; padding: 0; box-sizing: border-box; }
  html, body { width: 1200px; height: 893px; overflow: hidden; }
  body {
    background: var(--backdrop);
    font-family: "Questrial", "Century Gothic", sans-serif;
    position: relative;
  }
  .letterhead {
    position: absolute;
    left: 270px; top: 20px;
    width: 660px; height: 853px;
    background: var(--paper);
    box-shadow: 0 6px 24px rgba(53, 92, 152, 0.18);
    overflow: hidden;
  }
  .header-band { position: absolute; left: 0; top: 0; width: 660px; height: 200px; }
  .brand {
    position: absolute; left: 200px; top: 46px;
    display: flex; align-items: center; gap: 12px;
    color: var(--paper);
  }
  .brand-dot { width: 34px; height: 34px; border: 3px solid var(--paper); border-radius: 50%; }
  .brand-name { font-size: 34px; letter-spacing: 0.5px; }
  .brand-address {
    position: absolute; left: 222px; top: 100px;
    color: var(--paper); font-size: 10px;
  }
  .letter-body {
    position: absolute; left: 70px; top: 230px; width: 520px;
    color: var(--ink); font-size: 12.5px; line-height: 1.62;
  }
  .letter-body p { margin-bottom: 22px; }
  .signature {
    position: absolute; right: 60px; top: 660px; width: 210px;
    text-align: right; color: var(--ink);
    border-bottom: 1.5px solid var(--brand-blue); padding-bottom: 6px;
  }
  .signature-name { font-size: 15px; }
  .signature-title { font-size: 10.5px; margin-top: 2px; }
  .footer {
    position: absolute; left: 50px; right: 50px; top: 770px;
    border-top: 1.5px solid var(--brand-blue);
  }
  .footer-url {
    position: absolute; left: 50%; top: -13px; transform: translateX(-50%);
    background: var(--brand-blue); color: var(--paper);
    font-size: 11px; letter-spacing: 3px;
    padding: 5px 22px; border-radius: 14px;
  }
  .footer-contacts {
    position: absolute; left: 0; right: 0; top: 26px;
    display: flex; justify-content: center; gap: 30px;
    color: var(--brand-blue); font-size: 11px;
  }
  .contact { display: flex; align-items: center; gap: 6px; }
  .contact svg { width: 12px; height: 12px; }
</style>
</head>
<body>
  <main class="letterhead">
    <svg class="header-band" viewBox="0 0 660 200" aria-hidden="true">
      <path d="M0 0 H660 V8 Q430 250 0 110 Z" fill="var(--brand-blue)"/>
    </svg>
    <div class="brand">
      <span class="brand-dot"></span>
      <span class="brand-name">Brightpath Desk</span>
    </div>
    <div class="brand-address">240 Harbor Lane NE, Suite C-7, Marlow, GA 30400</div>

    <section class="letter-body">
      <p>Lorem ipsum dolor sit amet, consectetur adipiscing elit. Donec orci purus, luctus vitae dignissim eu, iaculis sed purus. Vivamus faucibus, ipsum nec aliquet viverra, leo mauris condimentum ligula, sit amet sagittis enim ligula quis arcu. Nam egestas tortor id nisi porttitor mattis. In tortor ante, ultricies in suscipit a, tempus non massa. Vivamus et auctor mi. Fusce vel massa nulla. Phasellus nec eros mauris, et scelerisque orci. Donec malesuada orci vitae nulla accumsan porta a id massa.</p>
      <p>Quisque accumsan iaculis magna sit amet fringilla. Maecenas consequat, magna eget tincidunt semper, odio nibh rutrum mi, id feugiat ante nisi eu risus. Vestibulum nunc orci, rhoncus a placerat in, ultricies in mi. Cras mattis varius eros, vel fringilla nisi suscipit eget. Quisque scelerisque sagittis nulla at porttitor. Mauris a justo et tellus interdum tristique. Sed id augue vitae urna euismod commodo aliquet a quam. Pellentesque arcu velit, cursus et malesuada ut, consequat et diam. Nullam erat sem, rhoncus id ullamcorper vitae, rhoncus et arcu. In ultricies ultricies nulla.</p>
      <p>Kut rutrum nisi iaculis at. Donec eu magna a metus ornare faucibus. Fusce aliquet faucibus ultricies. Morbi semper, est id tincidunt gravida, sem arcu adipiscing lacus, ac bibendum nulla leo eu purus. Quisque nec diam sed risus consectetur a accumsan quis quis nibh. Vestibulum id purus lorem. Donec eu magna a metus ornare faucibus. Fusce aliquet faucibus ultricies. Morbi semper, est id tincidunt gravida, sem arcu adipiscing lacus, ac bibendum nulla leo eu purus. Quisque nec diam sed risus consectetur a ccumsan quis quis nibh. Vestibulum id purus lorem.</p>
    </section>

    <div class="signature">
      <div class="signature-name">Owen Hale</div>
      <div class="signature-title">Co-Founder &amp; CEO</div>
    </div>

    <footer class="footer">
      <div class="footer-url">www.brightpathdesk.com</div>
      <div class="footer-contacts">
        <span class="contact">
          <svg viewBox="0 0 12 12" aria-hidden="true"><rect x="3" y="1" width="6" height="10" rx="1.5" fill="var(--brand-blue)"/></svg>
          555 210-4400
        </span>
        <span class="contact">
          <svg viewBox="0 0 12 12" aria-hidden="true"><path d="M1 5 Q6 0 11 5 L9 7 L8 5.5 Q6 4.8 4 5.5 L3 7 Z M3 8 H9 V11 H3 Z" fill="var(--brand-blue)"/></svg>
          555 318 2290
        </span>
        <span class="contact">
          <svg viewBox="0 0 12 12" aria-hidden="true"><rect x="1" y="2.5" width="10" height="7" rx="1" fill="var(--brand-blue)"/><path d="M1.5 3 L6 6.5 L10.5 3" stroke="var(--paper)" fill="none" stroke-width="1"/></svg>
          ohale@brightpathdesk.com
        </span>
      </div>
    </footer>
  </main>
</body>
</html>
```